PEACFUL ACUPUNCTURE PRACTITIONER NEEDS A NEW COAT

I need a new design for an exiting website http://willowgateneedlework.com/ for a acupuncturist. This will be a minimalism design with lots and lots of white space. Home page and one interior page. Please keep the feeling of calm and peaceful serenity. For Color scheme: https://www.morningfernclinic.com/fertility. The bottom part of the home page with sections and links to the service pages: https://harborlotuswellness.com/. The client likes this the best: http://mfclinic.com/. I'm attaching the logo and content pages.

Target Market(s)

Women

Industry/Entity Type

Wellness, health, wellbeing, meditation

Number of Pages Required

2 page

Font styles to use
Sans Serif
Decorative

Colors

Designer to choose colors to be used in the design.

Requirements
Must have
Nice to have
• Follow new website drafts and links
Should not have
• Busy with bright colors. No poping

```html
<!DOCTYPE html>
<html lang="en">
<head>
<meta charset="utf-8">
<title>Willowgate Acupuncture</title>
<link href="https://fonts.googleapis.com/css2?family=Crimson+Text:wght@400;600&family=Lato:wght@400;700&display=swap" rel="stylesheet">
<style>
:root{
  --rose:#bb8c92;
  --rose-dark:#a8767d;
  --rose-soft:#d7bfc2;
  --rose-pale:#e7d6d8;
  --grey-bg:#f0efef;
  --ink:#2d2a2b;
  --text:#4a4546;
  --muted:#8d8587;
  --white:#ffffff;
}
*{margin:0;padding:0;box-sizing:border-box}
html,body{width:1200px;height:3834px;overflow:hidden}
body{position:relative;background:var(--white);font-family:'Lato',sans-serif;color:var(--text)}
.abs{position:absolute}
.serif{font-family:'Crimson Text',serif}
.btn{position:absolute;background:var(--rose);color:var(--white);font-family:'Crimson Text',serif;font-weight:600;font-size:15px;border-radius:24px;display:flex;align-items:center;justify-content:center}
.section{position:absolute;left:0;width:1200px}

/* header */
.header{top:0;height:83px;background:var(--white)}
.search{left:112px;top:18px;width:280px;height:45px;border-radius:23px;box-shadow:0 2px 10px rgba(0,0,0,.12);background:var(--white);font-size:13px;color:var(--muted);padding-left:24px;display:flex;align-items:center}
.search svg{position:absolute;right:26px;top:15px}
.logo-tab{left:490px;top:0;width:220px;height:130px;z-index:5}
.logo{left:500px;top:8px;width:200px;text-align:center;z-index:6;color:#5a4a4c;font-family:'Crimson Text',serif}
.logo .dot{width:40px;height:40px;border-radius:50%;background:var(--rose-soft);margin:0 auto 4px}
.logo .name{font-size:27px;line-height:26px}
.logo .sub{font-size:14px;letter-spacing:3px;line-height:16px}
.social{top:26px;width:33px;height:33px;border-radius:50%;border:1.5px solid var(--rose)}
.social.fill{background:var(--rose)}
.contact{left:956px;top:22px;width:132px;height:35px;font-size:14px}

/* hero */
.hero{top:83px;height:620px;background:linear-gradient(120deg,#7f6a55 0%,#a79274 35%,#6a5a4c 60%,#3a3330 80%,#5b4f48 100%)}
.nav{left:112px;top:45px;width:976px;height:52px;background:rgba(188,140,146,.85);display:flex;align-items:center;font-size:15px;color:var(--white)}
.nav span{padding:0 15px;height:52px;display:flex;align-items:center}
.nav .active{background:#e5a7ae}
.hero h1{left:112px;top:193px;font-family:'Crimson Text',serif;font-weight:400;font-size:40px;line-height:42px;color:var(--white);letter-spacing:.5px}
.hero p{left:112px;top:296px;width:440px;font-size:15px;line-height:23px;color:var(--white)}
.hero .btn{left:112px;top:364px;width:126px;height:44px}
.dots{left:1130px;top:262px}
.dots i{display:block;width:11px;height:11px;border-radius:50%;background:var(--white);margin-bottom:11px}
.dots i.on{background:none;border:1.5px solid var(--white)}

/* services */
.service{position:absolute;top:595px;width:220px;text-align:center}
.service .ring{width:204px;height:204px;margin:0 auto;border-radius:50%;border:5px solid var(--rose);background:var(--white);padding:8px}
.service .photo{width:100%;height:100%;border-radius:50%}
.service h3{font-family:'Crimson Text',serif;font-weight:400;font-size:22px;color:var(--ink);margin-top:23px}
.service p{font-size:15px;line-height:22.5px;margin-top:8px;color:var(--text)}
.service .btn{position:relative;width:124px;height:40px;margin:18px auto 0}

/* about */
.about{top:1075px;height:554px;background:var(--grey-bg)}
.about .art{left:105px;top:48px;width:450px;height:450px;border-radius:50%;background:radial-gradient(circle,#c99da0 0%,#dcbcbe 55%,rgba(240,239,239,0) 72%)}
.about h2{left:625px;top:90px;font-family:'Crimson Text',serif;font-weight:400;font-size:34px;color:var(--ink)}
.about p{left:625px;top:147px;width:465px;font-size:14.5px;line-height:26.6px}
.about .btn{left:625px;top:403px;width:122px;height:41px}

/* fertility */
.fert{top:1629px;height:627px;background:var(--rose-soft)}
.fert h2{left:0;width:1200px;top:76px;text-align:center;font-family:'Crimson Text',serif;font-weight:400;font-size:34px;color:var(--ink)}
.card{position:absolute;top:156px;width:309px;height:393px;background:var(--white);text-align:center}
.card .photo{height:215px}
.card .icon{position:absolute;left:117px;top:177px;width:76px;height:76px;border-radius:50%;background:var(--rose);border:4px solid var(--white)}
.card h3{margin-top:48px;font-family:'Crimson Text',serif;font-weight:400;font-size:25px;color:var(--ink)}
.card p{font-size:14.5px;line-height:26.5px;margin:8px 30px 0}
.card a{display:block;margin-top:6px;font-family:'Crimson Text',serif;font-size:15px;color:var(--rose)}

/* hormone */
.hormone{top:2256px;height:618px;background:var(--grey-bg)}
.hormone h2{left:115px;top:178px;font-family:'Crimson Text',serif;font-weight:400;font-size:34px;color:var(--ink)}
.hormone p{left:115px;top:234px;width:470px;font-size:14.5px;line-height:26.6px}
.hormone .btn{left:112px;top:389px;width:123px;height:41px}
.hormone .photo{left:652px;top:88px;width:432px;height:442px;border-radius:8px;background:linear-gradient(135deg,#f0d0bd,#d9a78a 60%,#c48f74)}

/* testimonials */
.testi{top:2874px;height:551px;background:var(--rose-pale)}
.testi h2{left:0;width:1200px;top:80px;text-align:center;font-family:'Crimson Text',serif;font-weight:400;font-size:34px;color:var(--ink)}
.quote{position:absolute;top:166px;width:471px;height:300px;background:var(--white);border-radius:6px;text-align:center}
.quote .mark{font-family:'Crimson Text',serif;font-size:90px;line-height:60px;height:48px;margin-top:34px;color:var(--rose-soft);font-weight:600}
.quote p{font-size:14.5px;line-height:26px;margin:20px 28px 0}
.quote .avatar{width:60px;height:60px;border-radius:50%;background:linear-gradient(#a49492,#5e5250);margin:14px auto 0}
.quote h4{font-family:'Crimson Text',serif;font-weight:400;font-size:18px;color:var(--ink);margin-top:10px}
.arrow{top:300px;font-size:22px;color:var(--ink)}

/* footer */
.foot h5{position:absolute;top:3498px;font-size:20px;font-weight:400;letter-spacing:.5px;color:var(--ink)}
.hours{left:112px;top:3563px;width:315px}
.hours div{display:flex;justify-content:space-between;height:44px;align-items:center;border-bottom:1px solid #e5dcdd;font-size:14.5px;color:var(--muted)}
.hours div span:last-child{color:var(--rose)}
.insta{left:490px;top:3557px;display:grid;grid-template-columns:repeat(4,64px);gap:4px}
.insta i{display:block;height:64px}
.news{left:816px;top:3553px;width:272px;height:47px;background:#f3f1f1;font-size:15px;color:var(--muted);padding-left:21px;display:flex;align-items:center}
.news svg{position:absolute;right:14px;top:15px}
.rule{left:112px;top:3752px;width:976px;height:1px;background:#e3dcdd}
.copy{left:0;width:1200px;top:3783px;text-align:center;font-size:14.5px;color:var(--text)}
</style>
</head>
<body>

<header class="section header">
  <div class="abs search">Search
    <svg width="14" height="14" viewBox="0 0 14 14"><circle cx="6" cy="6" r="4.5" fill="none" stroke="#8d8587" stroke-width="1.6"/><line x1="9.3" y1="9.3" x2="13" y2="13" stroke="#8d8587" stroke-width="1.6"/></svg>
  </div>
  <span class="abs social fill" style="left:759px"></span>
  <span class="abs social" style="left:801px"></span>
  <span class="abs social" style="left:841px"></span>
  <span class="abs social" style="left:881px"></span>
  <div class="btn contact">Contact Us</div>
</header>

<svg class="abs logo-tab" viewBox="0 0 220 130"><polygon points="0,0 220,0 220,83 190,130 30,130 0,83" fill="#fff"/></svg>
<div class="abs logo">
  <div class="dot"></div>
  <div class="name">Willowgate</div>
  <div class="sub">ACUPUNCTURE</div>
</div>

<section class="section hero" role="img" aria-label="Acupuncture needles resting on a dark wooden block over a bamboo mat">
  <nav class="abs nav">
    <span class="active">Home</span><span>About Maren</span><span>Treatments</span><span>Health Concerns</span><span>Fertility</span><span>Pregnancy</span><span>Questions</span><span>Shop</span><span>Testimonials</span><span>Contact</span>
  </nav>
  <h1 class="abs">Welcome To Willowgate<br>Acupuncture</h1>
  <p class="abs">Acupuncture &amp; Chinese Herbal Medicine are rooted in over 3000 years of history and tradition.</p>
  <div class="btn">Learn More</div>
  <div class="abs dots"><i class="on"></i><i></i><i></i><i></i></div>
</section>

<div class="service" style="left:106px">
  <div class="ring"><div class="photo" role="img" aria-label="Pregnant woman resting on a sofa" style="background:linear-gradient(135deg,#b9b2ad,#cf8a52)"></div></div>
  <h3>fertility &amp; pregnancy</h3>
  <p>Lorem ipsum dolor sit amet, consectetur adipiscing elit, sed do eiusmo.</p>
  <div class="btn">Learn More</div>
</div>
<div class="service" style="left:363px">
  <div class="ring"><div class="photo" role="img" aria-label="Woman relaxing outdoors with eyes closed" style="background:linear-gradient(135deg,#9fb27f,#5b4b4b)"></div></div>
  <h3>Emotional Well Being</h3>
  <p>Lorem ipsum dolor sit amet, consectetur adipiscing elit, sed do eiusmo.</p>
  <div class="btn">Learn More</div>
</div>
<div class="service" style="left:621px">
  <div class="ring"><div class="photo" role="img" aria-label="Acupuncture needles placed in a bare shoulder" style="background:linear-gradient(135deg,#3c3634,#c9a08a)"></div></div>
  <h3>Hormone Balance</h3>
  <p>Lorem ipsum dolor sit amet, consectetur adipiscing elit, sed do eiusmo.</p>
  <div class="btn">Learn More</div>
</div>
<div class="service" style="left:879px">
  <div class="ring"><div class="photo" role="img" aria-label="Assorted dried Chinese herbs on a board" style="background:linear-gradient(135deg,#d9c9a8,#8a3f3a)"></div></div>
  <h3>Strength &amp; Structure</h3>
  <p>Lorem ipsum dolor sit amet, consectetur adipiscing elit, sed do eiusmo.</p>
  <div class="btn">Learn More</div>
</div>

<section class="section about">
  <div class="abs art" role="img" aria-label="Soft rose lotus decoration with treatment photo"></div>
  <h2 class="abs">About Maren</h2>
  <p class="abs">Maren Holloway is a Massachusetts and California Licensed Acupuncturist and Herbalist as well as Nationally Certified in both Acupuncture and Herbal Medicine. She obtained her Masters Degree from Cedar Hollow University in Santa Cruz CA and has studied at the integrated hospital in Hang Zhou China. She has also done extensive study in Chi Nei Tsang in both the USA and Thailand. She worked for Linden Root Herb Company a leader of high quality, lab tested Chinese patented herbal formulas as a consultant to both Acupuncturists</p>
  <div class="btn">Learn More</div>
</section>

<section class="section fert">
  <h2 class="abs">Fertility &amp; Pregnancy</h2>
  <div class="card" style="left:112px">
    <div class="photo" role="img" aria-label="Clinic sign on a brick wall beside green trees" style="background:linear-gradient(90deg,#7a4a3c 45%,#8fae6e)"></div>
    <div class="icon"></div>
    <h3>Fertility</h3>
    <p>Whether you are attempting to conceive at home.</p>
    <a>Leran More</a>
  </div>
  <div class="card" style="left:445px">
    <div class="photo" role="img" aria-label="Woman receiving cupping therapy on her back" style="background:linear-gradient(135deg,#7a5040,#c99778 60%,#5a3a2c)"></div>
    <div class="icon"></div>
    <h3>Conception at home/ICI</h3>
    <p>Difficulties tracking your cycle or repeated unsuccessful.</p>
    <a>Leran More</a>
  </div>
  <div class="card" style="left:779px">
    <div class="photo" role="img" aria-label="Herbal pills, cucumber slices and needles on wood" style="background:linear-gradient(135deg,#6f8f3a,#a07a4c 60%,#d8d2c8)"></div>
    <div class="icon"></div>
    <h3>IUI and IVF</h3>
    <p>Recent studies confirm Traditional Chinese Medicine's positive.</p>
    <a>Leran More</a>
  </div>
</section>

<section class="section hormone">
  <h2 class="abs">Hormone Balance</h2>
  <p class="abs">Our hormones are constantly shifting and occasionally this internal orchestra needs to be refined. Acupuncture works to help the body rediscover the positive patterns that lead to improved health and well being. By repeating these patterns we are reminding the body how to access greater health on its own.</p>
  <div class="btn">Learn More</div>
  <div class="abs photo" role="img" aria-label="Glass cupping jars on a patient's back"></div>
</section>

<section class="section testi">
  <h2 class="abs">Client Testimonials</h2>
  <span class="abs arrow" style="left:44px">&#8249;</span>
  <span class="abs arrow" style="left:1140px">&#8250;</span>
  <div class="quote" style="left:110px">
    <div class="mark">&ldquo;</div>
    <p>Maren is such an incredibly skilled, competent and knowl-edgeable practitioner. I started seeing Maren because after a year and a half of trying to conceive</p>
    <div class="avatar" role="img" aria-label="Client portrait"></div>
    <h4>L Baby Born 2017</h4>
  </div>
  <div class="quote" style="left:616px">
    <div class="mark">&ldquo;</div>
    <p>When I first came to Maren's office I was very desperate and pretty hopeless. I had been trying to conceive for close to three years and had had 4 failed IUIs.</p>
    <div class="avatar" role="img" aria-label="Client portrait"></div>
    <h4>L Baby Born 2017</h4>
  </div>
</section>

<footer class="foot">
  <h5 style="left:112px">HOURS</h5>
  <h5 style="left:494px">INSTAGRAM FEED</h5>
  <h5 style="left:817px">NEWSLETTER</h5>
  <div class="abs hours">
    <div><span>Tuesday:</span><span>10pm-6pm</span></div>
    <div><span>Friday:</span><span>10pm-6pm</span></div>
    <div><span>Saturday:</span><span>10pm-3pm</span></div>
  </div>
  <div class="abs insta" role="img" aria-label="Grid of eight clinic photos">
    <i style="background:#7b5a4a"></i><i style="background:#c9a060"></i><i style="background:#4f6a8a"></i><i style="background:#8e8a86"></i>
    <i style="background:#d3a48a"></i><i style="background:#b08a7a"></i><i style="background:#a0684a"></i><i style="background:#5a4a3a"></i>
  </div>
  <div class="abs news">Enter Your Email
    <svg width="16" height="16" viewBox="0 0 16 16"><path d="M15 1 1 7l6 2 2 6z M7 9l8-8" fill="none" stroke="#bb8c92" stroke-width="1.3" stroke-linejoin="round"/></svg>
  </div>
  <div class="abs rule"></div>
  <div class="abs copy">&copy;Copyrights 2021 Company Name &nbsp;| &nbsp; All Rights Reserved</div>
</footer>

</body>
</html>
```